Business Card Project for Keel Ridge Hoisting

Business name is "Keel Ridge Hoisting" we are a scaffolding & rigging business specialising in local and remote work for:
- scaffolding (residential, commercial, industrial)
- rigging
-man material hoists
- swing stages
- labour hire

On the back of the card I would like KRH as the symbol / logo. I have attached the logos we have had created by pixel harbour. We would like to use bold colours – preferably as the same colour scheme as the logo.

Target Market(s)

Construction business

Industry/Entity Type

Construction

Contact Information for Business Card

name: Miles Fenwick
Title: Director
Phone: 0491 572 846
Address: PO BOX 4821, Ternvale SA 5197
Email: miles@keelridgehoisting.com.au
Website: www.keelridgehoisting.com.au

Font styles to use
Sans Serif

Requirements
Must have
• Must use existing logo & prefering using bold colours
Nice to have
• Would be nice to have a line of dot points in what we specialise in but not essential
• Would be nice to see some designs with a slogan but not essential
Should not have
• NA

```html
<!DOCTYPE html>
<html lang="en">
<head>
<meta charset="utf-8">
<title>Keel Ridge Hoisting – Business Card</title>
<link rel="stylesheet" href="https://fonts.googleapis.com/css2?family=Montserrat:wght@400;500;700;800&family=Michroma&display=swap">
<style>
  :root {
    --ink: #0b0b0b;
    --paper: #ffffff;
    --blue: #1a73c2;
    --stage: #2b2b2b;
    --muted: #e9e9e9;
  }
  * { box-sizing: border-box; margin: 0; padding: 0; }
  html, body { width: 1200px; height: 900px; overflow: hidden; }
  body {
    background: var(--stage);
    font-family: "Montserrat", Arial, sans-serif;
    position: relative;
  }
  .card {
    position: absolute;
    left: 250px;
    width: 700px;
    height: 400px;
    border-radius: 28px;
    overflow: hidden;
  }
  /* Front */
  .card-front { top: 35px; background: var(--paper); }
  .front-brand {
    position: absolute;
    left: 200px; top: 70px;
    font-weight: 800;
    font-size: 120px;
    letter-spacing: 4px;
    color: var(--ink);
    line-height: 1;
  }
  .front-scope {
    position: absolute;
    left: 330px; top: 170px;
    font-size: 15px;
    font-weight: 500;
    color: var(--ink);
  }
  .services {
    position: absolute;
    left: 90px; top: 250px;
    list-style: none;
    font-size: 19px;
    font-weight: 500;
    color: var(--ink);
    line-height: 1.3;
  }
  .services li::before {
    content: "-- ";
    color: var(--blue);
  }
  /* Back */
  .card-back { top: 465px; background: var(--ink); }
  .back-strip {
    position: absolute;
    left: 0; top: 0; bottom: 0;
    width: 172px;
    background: var(--paper);
    border-right: 6px solid var(--blue);
  }
  .back-brand {
    position: absolute;
    left: 86px; top: 200px;
    transform: translate(-50%, -50%) rotate(-90deg);
    white-space: nowrap;
    font-weight: 800;
    font-size: 30px;
    color: var(--ink);
    letter-spacing: 1px;
  }
  .back-tab {
    position: absolute;
    right: 0; top: 40px;
    width: 24px; height: 115px;
    background: var(--blue);
    border-radius: 22px 0 0 22px;
  }
  .contact {
    position: absolute;
    right: 60px; top: 55px;
    text-align: right;
    color: var(--paper);
  }
  .contact-name {
    font-family: "Michroma", "Montserrat", sans-serif;
    font-size: 22px;
    color: var(--blue);
    letter-spacing: 1px;
  }
  .contact-role {
    font-family: "Michroma", "Montserrat", sans-serif;
    font-size: 14px;
    margin-top: 4px;
  }
  .contact-lines {
    list-style: none;
    margin-top: 14px;
    font-size: 16px;
    line-height: 1.55;
  }
  .contact-lines li { display: flex; justify-content: flex-end; align-items: center; gap: 10px; }
  .contact-lines .icon { width: 12px; height: 12px; flex: none; }
  .contact-lines .spacer { width: 12px; flex: none; }
  .web-domain { color: var(--blue); }
</style>
</head>
<body>
  <section class="card card-front" aria-label="Card front">
    <div class="front-brand">KRH</div>
    <p class="front-scope">(residential, commercial, industrial)</p>
    <ul class="services">
      <li>Scaffolding (residential, commercial, industrial)</li>
      <li>Rigging</li>
      <li>Man material hoists</li>
      <li>Swing stages</li>
      <li>Labour hire</li>
    </ul>
  </section>

  <section class="card card-back" aria-label="Card back">
    <div class="back-strip">
      <div class="back-brand">Keel Ridge Hoisting</div>
    </div>
    <div class="back-tab"></div>
    <div class="contact">
      <p class="contact-name">MILES FENWICK</p>
      <p class="contact-role">DIRECTOR</p>
      <ul class="contact-lines">
        <li>PO BOX 4821<span class="spacer"></span></li>
        <li>Ternvale SA 5197<span class="spacer"></span></li>
        <li>0491 572 846
          <svg class="icon" viewBox="0 0 12 12" aria-hidden="true"><path d="M2.5 1 L4.5 1 L5 3.5 L3.8 4.4 A6 6 0 0 0 7.6 8.2 L8.5 7 L11 7.5 L11 9.5 A1.5 1.5 0 0 1 9.5 11 A8.5 8.5 0 0 1 1 2.5 A1.5 1.5 0 0 1 2.5 1 Z" fill="var(--blue)"/></svg>
        </li>
        <li>miles@keelridgehoisting.com.au
          <svg class="icon" viewBox="0 0 12 12" aria-hidden="true"><rect x="1" y="2.5" width="10" height="7" rx="1" fill="none" stroke="var(--blue)" stroke-width="1.3"/><path d="M1.5 3 L6 6.5 L10.5 3" fill="none" stroke="var(--blue)" stroke-width="1.3"/></svg>
        </li>
        <li><span>www.<span class="web-domain">keelridgehoisting</span>.com.au</span>
          <svg class="icon" viewBox="0 0 12 12" aria-hidden="true"><circle cx="6" cy="6" r="5" fill="none" stroke="var(--blue)" stroke-width="1.2"/><ellipse cx="6" cy="6" rx="2.2" ry="5" fill="none" stroke="var(--blue)" stroke-width="1"/><path d="M1 6 H11" stroke="var(--blue)" stroke-width="1"/></svg>
        </li>
      </ul>
    </div>
  </section>
</body>
</html>
```